Business Card - Harlow Birch

Need Business Card design for company named Harlow Birch. Software development focused mainly on Ardel eKallo & oBix Apps. I've attached our logo with both a black and white background. Please add trademark symbol to logo when using.

```html
<!DOCTYPE html>
<html lang="en">
<head>
<meta charset="utf-8">
<title>Harlow Birch – Business Card</title>
<link rel="stylesheet" href="https://fonts.googleapis.com/css2?family=Open+Sans:wght@400;600;700&display=swap">
<style>
  :root {
    --stage: #e9e9ee;
    --card: #050505;
    --orange: #ff9a33;
    --gold: #f5b800;
    --white: #ffffff;
    --rule: #6a6a6a;
  }
  * { margin: 0; padding: 0; box-sizing: border-box; }
  html, body { width: 1200px; height: 987px; overflow: hidden; }
  body {
    background: var(--stage);
    font-family: "Open Sans", Arial, sans-serif;
    position: relative;
  }
  .card {
    position: absolute;
    width: 540px;
    height: 309px;
    background: var(--card);
    border-radius: 30px;
    overflow: hidden;
    top: 339px;
  }
  .card--front { left: 40px; }
  .card--back { left: 620px; }

  .swoosh { position: absolute; inset: 0; width: 100%; height: 100%; }

  .brand {
    position: absolute;
    display: flex;
    align-items: center;
    gap: 10px;
    color: var(--white);
    font-weight: 700;
    letter-spacing: -0.5px;
    white-space: nowrap;
  }
  .brand__dot {
    width: 14px; height: 14px;
    border-radius: 50%;
    background: var(--orange);
  }
  .card--front .brand { left: 40px; top: 52px; font-size: 34px; }
  .card--back .brand { left: 0; right: 0; justify-content: center; top: 100px; font-size: 40px; }

  .website {
    position: absolute;
    left: 0; right: 0; top: 172px;
    text-align: center;
    color: var(--white);
    font-size: 18px;
    letter-spacing: 2.5px;
  }

  .divider {
    position: absolute;
    left: 318px; top: 118px;
    width: 1px; height: 110px;
    background: var(--rule);
  }
  .contact { position: absolute; left: 336px; top: 118px; color: var(--white); }
  .contact__name { color: var(--gold); font-weight: 700; font-size: 20px; line-height: 1.1; }
  .contact__title { font-size: 16px; margin-bottom: 10px; }
  .contact__line { display: flex; align-items: center; gap: 10px; font-size: 17px; line-height: 1.5; }
  .contact__line svg { width: 14px; height: 14px; fill: var(--gold); }

  .address {
    position: absolute;
    left: 40px; bottom: 28px;
    color: var(--white);
    font-size: 17px;
    line-height: 1.3;
  }
</style>
</head>
<body>
  <section class="card card--front">
    <svg class="swoosh" viewBox="0 0 540 309" preserveAspectRatio="none" aria-hidden="true">
      <path d="M0,120 C50,185 130,222 260,245 C380,266 470,272 515,309 L0,309 Z" fill="var(--orange)"/>
      <path d="M0,150 C60,200 150,232 270,252 C390,272 470,280 505,309" fill="none" stroke="var(--card)" stroke-width="4"/>
    </svg>

    <div class="brand"><span class="brand__dot"></span>Harlow Birch™</div>

    <div class="divider"></div>
    <div class="contact">
      <div class="contact__name">Your Name</div>
      <div class="contact__title">Title</div>
      <div class="contact__line">
        <svg viewBox="0 0 14 14" aria-hidden="true"><rect x="3" y="0" width="8" height="14" rx="1.5"/></svg>
        555-010-4821
      </div>
      <div class="contact__line">
        <svg viewBox="0 0 14 14" aria-hidden="true"><path d="M1,7 C1,3 13,3 13,7 L11,7 L11,5.5 L3,5.5 L3,7 Z M2,8 L12,8 L12,13 L2,13 Z"/></svg>
        555-010-7394
      </div>
    </div>

    <div class="address">4120 Alder Road N<br>Fernvale, FL 30912</div>
  </section>

  <section class="card card--back">
    <div class="brand"><span class="brand__dot"></span>Harlow Birch™</div>
    <div class="website">www.harlowbirch.com</div>
  </section>
</body>
</html>
```